Business Card Design - front and back

Residential real estate agent looking for a an emphasis on my first name (last name is hard to spell).  Would love the slogan "It's more than a contract" on the card.  Simple, easy to read business card that makes people want to pick it up and remember it.  The Bright Lantern Realty has to be on the front of card but does not need to be the emphasis.  Prefer locations on the back.  Would love a home on it.  Looking for simply elegant in the card that shows I am a non-complicated, warm, honest real estate agent.
NEED ONE OF MY PICTURES ON THE CARD.  LEAVING WHICH ONE UP TO THE DESIGNER.

Industry/Entity Type
Real Estate
Contact Information for Business Card
Gloria Penwick, Broker Associate, Bright Lantern Realty, 727-481-6054 cell, hereisgloria@maplenest.example, listedbygloria.example, Bright Lantern Realty locations: 48217 Orrington Blvd Ste 101, Tampa, FL  30918, 2948 Velo Ct Ste 101, New Port Richey, FL  30742
I NEED THIS DOUBLE SIDED - THE SELECTION BELOW WILL NOT ALLOW IT?
Requirements
Must have
- Emphasis on my first name
a home in it
LOVE Marla dobrin's logo which sits on the left side in the margin at
http://marladobrin.quillagentsite.example/
Something with that idea is exactly what I am looking for.
Nice to have
- Nice script that is readable.
Should not have
- I am looking for something simple

```html
<!DOCTYPE html>
<html lang="en">
<head>
<meta charset="UTF-8">
<title>Gloria Penwick – Business Card</title>
<link rel="stylesheet" href="https://fonts.googleapis.com/css2?family=Roboto+Condensed:wght@300;400;700&display=swap">
<style>
  :root {
    --stage: #e8e6e3;
    --brand-blue: #1677a8;
    --ink-dark: #333436;
    --paper: #ffffff;
    --muted-light: #d9dadb;
    --name-grey: #3a3b3d;
  }
  * { box-sizing: border-box; margin: 0; padding: 0; }
  html, body {
    width: 1200px; height: 864px; overflow: hidden;
    background: var(--stage);
    font-family: "Roboto Condensed", "Arial Narrow", sans-serif;
  }
  .card {
    position: absolute; left: 100px; top: 146px;
    width: 1000px; height: 572px;
    background: var(--brand-blue);
    box-shadow: 0 14px 34px rgba(0,0,0,0.22);
    overflow: hidden;
  }
  .brand {
    position: absolute; left: 96px; top: 148px;
    width: 560px;
  }
  .brand-lockup {
    display: flex; align-items: flex-end; gap: 22px;
  }
  .brand-square {
    flex: none;
    width: 112px; height: 112px;
    border: 3px solid var(--paper);
  }
  .brand-name {
    color: var(--paper);
    font-weight: 300;
    font-size: 44px;
    letter-spacing: 1px;
    text-transform: uppercase;
    line-height: 1;
    white-space: nowrap;
    padding-bottom: 2px;
  }
  .brand-rule {
    margin-top: 22px;
    height: 3px; width: 100%;
    background: var(--paper);
  }
  .name-band {
    position: absolute; left: 0; top: 362px;
    width: 100%; height: 62px;
    background: var(--paper);
    display: flex; align-items: center;
    padding: 0 40px 0 96px;
  }
  .phone {
    display: flex; align-items: center; gap: 12px;
    color: var(--ink-dark);
    font-size: 20px; font-weight: 400;
    white-space: nowrap;
  }
  .title {
    margin-left: 22px;
    color: var(--brand-blue);
    font-size: 19px; font-weight: 400;
    text-transform: uppercase;
    white-space: nowrap;
  }
  .agent-name {
    margin-left: auto;
    font-size: 36px;
    text-transform: uppercase;
    letter-spacing: 0.5px;
    white-space: nowrap;
  }
  .agent-first { color: var(--brand-blue); font-weight: 700; }
  .agent-last { color: var(--name-grey); font-weight: 300; }
  .contact-band {
    position: absolute; left: 0; top: 424px;
    width: 100%; height: 148px;
    background: var(--ink-dark);
    display: flex;
    padding: 34px 40px 0 96px;
    gap: 56px;
  }
  .contact-item {
    display: flex; gap: 16px;
    color: var(--muted-light);
    font-size: 19px; line-height: 1.45; font-weight: 300;
    white-space: nowrap;
  }
  .contact-item svg { flex: none; margin-top: 3px; }
  .contact-item.web { margin-left: auto; }
</style>
</head>
<body>
  <div class="card">
    <div class="brand">
      <div class="brand-lockup">
        <div class="brand-square"></div>
        <div class="brand-name">Bright Lantern Realty</div>
      </div>
      <div class="brand-rule"></div>
    </div>

    <div class="name-band">
      <div class="phone">
        <svg width="14" height="22" viewBox="0 0 14 22" aria-hidden="true">
          <rect x="1" y="1" width="12" height="20" rx="2" fill="none" stroke="#333436" stroke-width="2"/>
          <line x1="5" y1="17.5" x2="9" y2="17.5" stroke="#333436" stroke-width="1.6"/>
        </svg>
        <span>+1-727-481-6054</span>
      </div>
      <span class="title">Broker Associate</span>
      <div class="agent-name"><span class="agent-first">Gloria</span> <span class="agent-last">Penwick</span></div>
    </div>

    <div class="contact-band">
      <div class="contact-item">
        <svg width="20" height="18" viewBox="0 0 20 18" aria-hidden="true">
          <path d="M10 1 L19 9 H16 V17 H4 V9 H1 Z" fill="#d9dadb"/>
          <rect x="8" y="11" width="4" height="6" fill="#333436"/>
        </svg>
        <div>48217 Orrington Blvd<br>Ste 101, Tampa, FL 30918</div>
      </div>
      <div class="contact-item">
        <svg width="20" height="18" viewBox="0 0 20 18" aria-hidden="true">
          <path d="M10 1 L19 9 H16 V17 H4 V9 H1 Z" fill="#d9dadb"/>
          <rect x="8" y="11" width="4" height="6" fill="#333436"/>
        </svg>
        <div>2948 Velo Ct Ste 101,<br>New Port Richey, FL 30742</div>
      </div>
      <div class="contact-item web">
        <svg width="18" height="16" viewBox="0 0 18 16" aria-hidden="true">
          <rect x="1" y="1" width="16" height="14" rx="2" fill="none" stroke="#d9dadb" stroke-width="2"/>
        </svg>
        <div>hereisgloria@maplenest.example<br>www.listedbygloria.example</div>
      </div>
    </div>
  </div>
</body>
</html>
```